Social Media Post Quote #5 - Native American Organization

- CHERISH - must be included
- Protect your community. Protect Your Elders. Stay Vaccinated. must be included
- Attached, company Logo, campaign logos and sample flu social media image. - our audience likes BRIGHT colors.
- Must include image from the United States, representing Land/Nature from one of the following regions, Plains and Woodlands, or Southwest, or Mountains, or Coast.
- must include quote: Help our “early elders” achieve “older elders” status.
- One image will be provided twice - incorporating campaign logos - in some fashion
Inspiration: https://velmorhub.example/ and https://www.facebook.com/Velmorhub

```html
<!DOCTYPE html>
<html lang="en">
<head>
<meta charset="utf-8">
<title>CHERISH – COVID-19 Vaccination Campaign</title>
<link href="https://fonts.googleapis.com/css2?family=Roboto+Condensed:ital,wght@0,400;0,500;0,700;1,400;1,500;1,800&display=swap" rel="stylesheet">
<style>
  :root {
    --sky-blue: #4f9ed6;
    --sky-pale: #bfe0ea;
    --sun-yellow: #f7d24a;
    --sun-orange: #f3a24a;
    --haze-pink: #e27a7a;
    --ridge-rose: #b0577c;
    --ridge-plum: #6a3a63;
    --ground-dark: #1f1822;
    --campaign-red: #8e1b2c;
    --frame-white: rgba(255, 255, 255, 0.92);
    --panel-veil: rgba(255, 255, 255, 0.18);
    --quote-white: #ffffff;
    --brand-teal: #3aa7a8;
  }
  * { margin: 0; padding: 0; box-sizing: border-box; }
  html, body { width: 1200px; height: 1200px; overflow: hidden; }
  body { font-family: "Roboto Condensed", "Arial Narrow", sans-serif; }

  .post {
    position: relative;
    width: 1200px;
    height: 1200px;
    overflow: hidden;
  }
  .landscape {
    position: absolute;
    inset: 0;
    background:
      linear-gradient(180deg,
        var(--sky-blue) 0%,
        var(--sky-pale) 14%,
        var(--sun-yellow) 32%,
        var(--sun-orange) 44%,
        var(--haze-pink) 56%,
        var(--ridge-rose) 68%,
        var(--ridge-plum) 80%,
        var(--ground-dark) 100%);
  }
  .inner-frame {
    position: absolute;
    inset: 36px;
    border: 2px solid var(--panel-veil);
    box-shadow: 0 0 0 36px rgba(255, 255, 255, 0.1);
  }

  .campaign-mark {
    position: absolute;
    left: 287px;
    top: 97px;
    width: 621px;
    height: 190px;
    border: 5px solid var(--frame-white);
    border-bottom: none;
    text-align: center;
  }
  .campaign-name {
    font-weight: 500;
    font-size: 138px;
    line-height: 1;
    letter-spacing: 4px;
    color: var(--campaign-red);
    margin-top: 20px;
  }
  .campaign-label {
    position: absolute;
    left: 41px;
    right: 41px;
    top: 165px;
    height: 43px;
    background: var(--frame-white);
    color: var(--campaign-red);
    font-weight: 700;
    font-size: 30px;
    line-height: 43px;
    letter-spacing: 1.5px;
  }
  .tagline {
    position: absolute;
    top: 337px;
    width: 100%;
    text-align: center;
    font-weight: 500;
    font-size: 23px;
    color: var(--campaign-red);
    letter-spacing: 0.5px;
  }

  .quote {
    position: absolute;
    top: 466px;
    width: 100%;
    text-align: center;
    color: var(--quote-white);
    font-style: italic;
    font-size: 100px;
    line-height: 132px;
    letter-spacing: 5px;
  }
  .quote strong { font-weight: 800; }
  .quote span { font-weight: 500; }

  .brand {
    position: absolute;
    left: 78px;
    top: 1060px;
    display: flex;
    align-items: center;
    gap: 16px;
    color: var(--brand-teal);
    font-weight: 700;
    font-size: 40px;
    letter-spacing: 2px;
  }
  .brand-square {
    width: 34px;
    height: 34px;
    background: var(--brand-teal);
  }
</style>
</head>
<body>
  <main class="post">
    <div class="landscape" role="img" aria-label="Photograph of layered mountain ridges at sunset under a blue and golden sky"></div>
    <div class="inner-frame"></div>

    <header class="campaign-mark">
      <h1 class="campaign-name">CHERISH</h1>
      <p class="campaign-label">COVID -19 VACCINATION CAMPAIGN</p>
    </header>
    <p class="tagline">Protect your community. Protect Your Elders. Stay Vaccinated.</p>

    <blockquote class="quote">
      <strong>Help</strong> <span>our</span> <strong>"early elders"</strong><br>
      <strong>achieve</strong><br>
      <strong>"older elders"</strong> <span>status.</span>
    </blockquote>

    <footer class="brand">
      <div class="brand-square"></div>
      <span class="brand-name">VELMOR HUB</span>
    </footer>
  </main>
</body>
</html>
```